KB Rubbish Removal Business Card

Hey,
I need a double sided business card designed for a rubbish removal business based in Australia. Logo is already chosen, similar colours preferred for both sides of the business card.

Details to include:

Front:

KB Rubbish Removal
Darren Holloway
Managing Director
Mobile: 0471 902 146
Email: darren@kbrubbishremoval.com.au
Website: kbrubbishremoval.com.au

Rear:

How did we do?
kbrubbishremoval.com.au/review

```html
<!DOCTYPE html>
<html lang="en">
<head>
<meta charset="utf-8">
<title>KB Rubbish Removal Business Card</title>
<link href="https://fonts.googleapis.com/css2?family=Lato:wght@400;700;900&display=swap" rel="stylesheet">
<style>
  :root {
    --page: #ffffff;
    --green-deep: #15723a;
    --green-mid: #2fae4a;
    --green-lime: #9bc03e;
    --green-ink: #176e36;
    --white: #ffffff;
    --photo-top-a: #1f8a3a;
    --photo-top-b: #3aa845;
    --photo-bottom-a: #d9e02a;
    --photo-bottom-b: #8fc03f;
  }
  html, body {
    margin: 0;
    padding: 0;
    width: 820px;
    height: 1200px;
    overflow: hidden;
    background: var(--page);
    font-family: "Lato", Arial, sans-serif;
  }
  .canvas {
    position: relative;
    width: 820px;
    height: 1200px;
  }
  .card {
    position: absolute;
    left: 60px;
    width: 700px;
    height: 400px;
    overflow: hidden;
    box-shadow: 0 4px 14px rgba(0,0,0,0.25);
    background: var(--white);
  }
  .card--front { top: 170px; }
  .card--back { top: 630px; }
  .card__art {
    position: absolute;
    inset: 0;
    width: 700px;
    height: 400px;
  }
  .emblem {
    position: absolute;
    left: 30px;
    top: 106px;
    width: 216px;
    height: 216px;
    display: flex;
    align-items: center;
    justify-content: center;
    text-align: center;
    font-weight: 900;
    font-size: 26px;
    line-height: 1.15;
    color: var(--green-ink);
  }
  .holder {
    position: absolute;
    left: 323px;
    top: 44px;
    color: var(--white);
  }
  .holder__name {
    display: flex;
    align-items: center;
    gap: 10px;
    margin-left: -35px;
    font-weight: 900;
    font-size: 30px;
    letter-spacing: -0.2px;
  }
  .holder__role {
    margin-top: 2px;
    font-size: 22px;
    font-weight: 400;
  }
  .company {
    position: absolute;
    font-weight: 900;
    font-size: 41px;
    letter-spacing: -0.5px;
    color: var(--green-ink);
    white-space: nowrap;
  }
  .card--front .company { left: 283px; top: 187px; }
  .card--back .company { left: 291px; top: 187px; }
  .contacts {
    position: absolute;
    left: 286px;
    top: 282px;
    margin: 0;
    padding: 0;
    list-style: none;
    color: var(--white);
    font-size: 23px;
    font-weight: 700;
  }
  .contacts li {
    display: flex;
    align-items: center;
    gap: 10px;
    height: 31px;
  }
  .contacts svg { flex: none; }
  .review {
    position: absolute;
    left: 296px;
    top: 300px;
    color: var(--white);
    text-shadow: 0 1px 3px rgba(0,60,20,0.45);
  }
  .review__ask {
    font-size: 23px;
    font-weight: 900;
    line-height: 31px;
  }
  .review__link {
    font-size: 23px;
    font-weight: 700;
    line-height: 31px;
  }
</style>
</head>
<body>
<main class="canvas">

  <section class="card card--front" aria-label="Business card front">
    <svg class="card__art" viewBox="0 0 700 400" aria-hidden="true">
      <defs>
        <linearGradient id="front-top" x1="0" y1="0" x2="0" y2="1">
          <stop offset="0" stop-color="var(--green-deep)"/>
          <stop offset="1" stop-color="var(--green-mid)"/>
        </linearGradient>
      </defs>
      <path d="M0 0 H700 V143 C600 170 450 177 265 175 C150 170 60 130 0 94 Z" fill="url(#front-top)"/>
      <path d="M0 290 C120 292 200 262 265 260 C380 248 470 246 700 275 V400 H0 Z" fill="var(--green-lime)"/>
      <circle cx="138" cy="214" r="136" fill="var(--white)"/>
    </svg>
    <div class="emblem">KB Rubbish<br>Removal</div>

    <div class="holder">
      <div class="holder__name">
        <svg width="25" height="23" viewBox="0 0 24 22" aria-hidden="true"><circle cx="12" cy="6" r="5.5" fill="#fff"/><path d="M1 22 C1 14 23 14 23 22 Z" fill="#fff"/></svg>
        Darren Holloway
      </div>
      <div class="holder__role">Managing Director</div>
    </div>

    <div class="company">KB Rubbish Removal</div>

    <ul class="contacts">
      <li>
        <svg width="16" height="16" viewBox="0 0 16 16" aria-hidden="true"><path d="M3 1 L6 4 L4.5 6 C5.5 8.5 7.5 10.5 10 11.5 L12 10 L15 13 L13 15 C6.5 14.5 1.5 9.5 1 3 Z" fill="var(--green-ink)"/></svg>
        0471 902 146
      </li>
      <li>
        <svg width="16" height="12" viewBox="0 0 16 12" aria-hidden="true"><rect x="0.5" y="0.5" width="15" height="11" fill="var(--green-ink)"/><path d="M1 1 L8 7 L15 1 M1 11 L6 5.5 M15 11 L10 5.5" stroke="var(--green-lime)" stroke-width="1.2" fill="none"/></svg>
        darren@kbrubbishremoval.com.au
      </li>
      <li>
        <svg width="16" height="16" viewBox="0 0 16 16" aria-hidden="true"><g fill="none" stroke="var(--green-ink)" stroke-width="1.4"><circle cx="8" cy="8" r="7"/><ellipse cx="8" cy="8" rx="3" ry="7"/><path d="M1 8 H15 M2.5 4.5 H13.5 M2.5 11.5 H13.5"/></g></svg>
        kbrubbishremoval.com.au
      </li>
    </ul>
  </section>

  <section class="card card--back" aria-label="Business card back">
    <svg class="card__art" viewBox="0 0 700 400">
      <defs>
        <linearGradient id="back-top" x1="0" y1="0" x2="1" y2="1">
          <stop offset="0" stop-color="var(--photo-top-a)"/>
          <stop offset="1" stop-color="var(--photo-top-b)"/>
        </linearGradient>
        <linearGradient id="back-bottom" x1="0" y1="0" x2="1" y2="1">
          <stop offset="0" stop-color="var(--photo-bottom-a)"/>
          <stop offset="1" stop-color="var(--photo-bottom-b)"/>
        </linearGradient>
      </defs>
      <path role="img" aria-label="Photo of a backyard being cleared of rubbish, tinted green" d="M0 0 H700 V105 C600 160 450 175 265 175 C150 170 60 150 0 140 Z" fill="url(#back-top)"/>
      <path role="img" aria-label="Photo of a garden after rubbish removal, tinted yellow-green" d="M0 280 C120 270 200 255 265 250 C400 240 480 300 580 295 C640 292 680 285 700 280 V400 H0 Z" fill="url(#back-bottom)"/>
      <circle cx="138" cy="214" r="136" fill="var(--white)"/>
    </svg>
    <div class="emblem">KB Rubbish<br>Removal</div>
    <div class="company">KB Rubbish Removal</div>
    <div class="review">
      <div class="review__ask">How did we do?</div>
      <div class="review__link">kbrubbishremoval.com.au/review</div>
    </div>
  </section>

</main>
</body>
</html>
```